Creative Businesss Card desgin!

Create a business card for our business Gleam window cleaning!
We are open to creative ideas as long as it maintains a professional image.

Target Market(s)

Small Commercial window cleaning clients including car dealerships, strata manager, cafe

Industry/Entity Type

Window Cleaning

Contact Information for Business Card

Daniel Prescott
General Manager
Gleam Window Cleaning

daniel@gleamservices.com.au
pane-care-southbank.com.au
Ph: 1800 GET GLEAM
Mob: 0437 582 061

Colors
fbed22
0392cd

Requirements
Should not have
• Stock window cleaning/ squeegee graphics

```html
<!DOCTYPE html>
<html lang="en">
<head>
<meta charset="utf-8">
<title>Gleam Window Cleaning – Business Card</title>
<link href="https://fonts.googleapis.com/css2?family=Open+Sans:wght@300;400;600;700&display=swap" rel="stylesheet">
<style>
  :root {
    --blue: #0d5c96;
    --blue-deep: #0a4f82;
    --yellow: #f4ec22;
    --yellow-soft: #ddd41c;
    --white: #ffffff;
    --ink: #2b2b2b;
    --page: #2a2d31;
  }
  * { margin: 0; padding: 0; box-sizing: border-box; }
  html, body {
    width: 1200px;
    height: 900px;
    overflow: hidden;
    background: var(--page);
    font-family: "Open Sans", Arial, sans-serif;
  }
  .canvas {
    position: relative;
    width: 1200px;
    height: 900px;
  }
  .card {
    position: absolute;
    top: 296px;
    width: 540px;
    height: 309px;
    overflow: hidden;
    box-shadow: 0 14px 30px rgba(0,0,0,0.45);
  }
  .card--contact { left: 40px; background: var(--white); }
  .card--brand { left: 620px; background: var(--blue); }

  .card__shapes {
    position: absolute;
    inset: 0;
    width: 100%;
    height: 100%;
  }
  .shape--blue { fill: var(--blue); }
  .shape--yellow { fill: var(--yellow); }
  .shape--pattern { fill: var(--yellow-soft); }

  .identity {
    position: absolute;
    left: 40px;
    top: 58px;
    display: flex;
    align-items: flex-start;
    gap: 10px;
  }
  .identity__dot {
    width: 14px;
    height: 14px;
    margin-top: 8px;
    border-radius: 50%;
    background: var(--yellow);
  }
  .identity__name {
    color: var(--yellow);
    font-weight: 600;
    font-size: 22px;
    line-height: 1.1;
  }
  .identity__role {
    color: var(--white);
    font-weight: 300;
    font-size: 14px;
    margin-top: 2px;
  }

  .phones {
    position: absolute;
    left: 16px;
    top: 156px;
    list-style: none;
    color: var(--ink);
    font-size: 12px;
    line-height: 20px;
  }
  .phones li { display: flex; align-items: center; gap: 6px; }
  .phones svg { width: 11px; height: 11px; fill: none; stroke: var(--blue); stroke-width: 1.6; }
  .phones .icon-fill { fill: var(--blue); stroke: none; }

  .online {
    position: absolute;
    right: 52px;
    top: 232px;
    list-style: none;
    color: var(--ink);
    font-size: 14px;
    line-height: 26px;
    text-align: right;
  }
  .online li { display: flex; align-items: center; justify-content: flex-end; gap: 8px; }
  .online svg { width: 14px; height: 14px; }
  .icon-mail rect { fill: var(--blue); }
  .icon-mail path { fill: none; stroke: var(--white); stroke-width: 1.2; }
  .icon-web circle { fill: var(--blue); }
  .icon-web path { fill: none; stroke: var(--white); stroke-width: 1; }

  .brand {
    position: absolute;
    inset: 0;
    display: flex;
    flex-direction: column;
    align-items: center;
    justify-content: center;
    color: var(--yellow);
    font-weight: 700;
    text-transform: uppercase;
    line-height: 1;
  }
  .brand__name { font-size: 78px; letter-spacing: 2px; }
  .brand__service { font-size: 24px; letter-spacing: 3px; margin-top: 10px; }
</style>
</head>
<body>
<main class="canvas">

  <section class="card card--contact" aria-label="Business card, contact side">
    <svg class="card__shapes" viewBox="0 0 540 309" preserveAspectRatio="none" aria-hidden="true">
      <polygon class="shape--blue" points="0,0 432,0 389,179 119,309 0,309"/>
      <polygon class="shape--yellow" points="0,117 160,288 119,309 0,309"/>
    </svg>
    <svg class="card__shapes" viewBox="0 0 540 309" preserveAspectRatio="none" role="img" aria-label="Yellow panel with tonal bolt pattern">
      <polygon class="shape--yellow" points="432,0 540,0 540,232 389,179"/>
    </svg>

    <div class="identity">
      <span class="identity__dot"></span>
      <div>
        <p class="identity__name">Daniel Prescott</p>
        <p class="identity__role">General Manager</p>
      </div>
    </div>

    <ul class="phones">
      <li>
        <svg viewBox="0 0 12 12" aria-hidden="true"><path class="icon-fill" d="M2.5 0.8 L4.6 0.8 L5.2 3.6 L3.9 4.6 C4.6 6.1 5.9 7.4 7.4 8.1 L8.4 6.8 L11.2 7.4 L11.2 9.5 C11.2 10.5 10.4 11.2 9.4 11.1 C5 10.6 1.4 7 0.9 2.6 C0.8 1.6 1.5 0.8 2.5 0.8 Z"/></svg>
        <span>1800 GET GLEAM</span>
      </li>
      <li>
        <svg viewBox="0 0 12 12" aria-hidden="true"><rect x="3" y="0.8" width="6" height="10.4" rx="1"/></svg>
        <span>0437 582 061</span>
      </li>
    </ul>

    <ul class="online">
      <li>
        <span>daniel@gleamservices.com.au</span>
        <svg class="icon-mail" viewBox="0 0 14 14" aria-hidden="true"><rect x="0.5" y="2.5" width="13" height="9" rx="1"/><path d="M1 3 L7 8 L13 3"/></svg>
      </li>
      <li>
        <span>pane-care-southbank.com.au</span>
        <svg class="icon-web" viewBox="0 0 14 14" aria-hidden="true"><circle cx="7" cy="7" r="6.5"/><path d="M1 7 H13 M7 1 V13 M7 1 C4 4 4 10 7 13 M7 1 C10 4 10 10 7 13 M2 4 H12 M2 10 H12"/></svg>
      </li>
    </ul>
  </section>

  <section class="card card--brand" aria-label="Business card, brand side">
    <div class="brand">
      <span class="brand__name">Gleam</span>
      <span class="brand__service">Window Cleaning</span>
    </div>
  </section>

</main>
</body>
</html>
```